Stationary Design needed for luxorious bespoke tailor

We need a design for our stationary items like businescards, letters, envelope and letter head / Signature for email. Our company "VELMARDO" sells exclusively and luxourious bespoke garments and accessories for men. The desgins of letterhead, envelope and business card shoulderstand communicate luxury, high quality and good taste. We would like our logo to be used on the designs.

Target Market(s)

Gentleman with a high aproach and exclusive and luxourious suits and shirts, grooms, businesman,

Industry/Entity Type

It Company

Font styles to use
Sans Serif

Colors
ec1f27
ffffff

Requirements
Must have
• Logo, Companies name and adress, contactName internet & email, phone number line / mobile, VAT Nr. On Business Card frontpage only logo and name, adress companies on backpage. No VAT and Companies ID there. Company data; VELMARDO AG Sonnwiesweg 27 4068 Basel Switzerland VAT: CHE 472 916 503 Tax Tel 41 61 508 37 14 Mobile 41 79 842 07 91 www.velmardo.ch info@velmardo.com.
Nice to have
• -Name And phone numbers need to be able to change (for different coworkers ...)
Should not have
• no VAT in Business Card

```html
<!DOCTYPE html>
<html lang="de">
<head>
<meta charset="utf-8">
<title>VELMARDO – Geschäftsausstattung</title>
<link href="https://fonts.googleapis.com/css2?family=Montserrat:wght@400;500;600&display=swap" rel="stylesheet">
<style>
:root{
  --red:#ec1f27;
  --ink:#2a2a2d;
  --black:#151515;
  --paper:#f7f7f7;
  --stage:#e4e4e4;
  --muted:#5a6478;
  --white:#ffffff;
}
*{margin:0;padding:0;box-sizing:border-box}
html,body{width:1200px;height:1106px;overflow:hidden;background:var(--white)}
body{position:relative;font-family:"Montserrat",sans-serif;color:var(--ink)}
.stage{position:absolute;left:0;top:0;width:1200px;height:926px;background:var(--stage)}
.sheet{position:absolute;background:var(--paper)}
.brand{position:absolute;line-height:1}
.brand .name{display:block;font-weight:500;letter-spacing:.06em;color:var(--ink)}
.brand .tag{display:block;font-weight:500;color:var(--ink)}
.on-dark .name,.on-dark .tag{color:var(--white)}

/* letterhead */
.letterhead{left:190px;top:96px;width:368px;height:520px}
.letterhead .brand{left:42px;top:36px}
.letterhead .name{font-size:20px}
.letterhead .tag{font-size:5.6px;letter-spacing:.62em;margin-top:3px}
.recipient{position:absolute;left:42px;top:100px;font-size:6.6px;line-height:1.35}
.recipient p+p{margin-top:6px}
.date{position:absolute;right:37px;top:130px;font-size:6.6px}
.letter-body{position:absolute;left:42px;top:198px;width:294px;font-size:5.8px;line-height:1.42;text-align:justify}
.letter-body p{margin-bottom:8px}
.letter-body .greet,.letter-body .close{font-weight:600;font-size:6.4px}
.signer{position:absolute;left:264px;top:390px;font-size:6px;line-height:1.1}
.signer small{display:block;font-size:4px}
.signature{position:absolute;left:249px;top:400px;width:92px;height:34px;background:linear-gradient(90deg,#dfe3ee,#e9ecf3);border-radius:3px}
.letter-foot{position:absolute;left:18px;right:18px;top:584px}
.letter-foot .co{text-align:center;color:var(--red);font-size:6px;font-weight:600}
.letter-foot .rule{height:1px;background:var(--muted);margin:3px 0 3px}
.letter-foot .addr{font-size:4.4px;white-space:nowrap;text-align:center;color:var(--ink)}
/* positioned relative to sheet */
.letter-foot{top:488px}

/* folder */
.folder{left:622px;top:72px;width:434px;height:548px;background:var(--black)}
.folder .brand{left:0;right:0;top:102px;text-align:center}
.folder .name{font-size:34px;letter-spacing:.07em}
.folder .tag{font-size:9.6px;letter-spacing:.84em;margin-top:6px;padding-left:.84em}

/* business cards */
.card{width:166px;height:94px}
.card-front{left:56px;top:663px;background:var(--black)}
.card-front .brand,.card-back .brand{left:0;right:0;text-align:center}
.card-front .brand{top:38px}
.card .name{font-size:14px}
.card .tag{font-size:4.2px;letter-spacing:.72em;margin-top:2px;padding-left:.72em}
.card-back{left:56px;top:784px}
.card-back .brand{top:14px}
.card-person{position:absolute;left:27px;top:51px;font-size:6.6px;font-weight:500}
.card-contact{position:absolute;top:67px;font-size:3.9px;line-height:1.2}
.card-contact.left{left:27px}
.card-contact.right{left:94px}
.card-contact li{list-style:none;display:flex;align-items:center;gap:3px}
.dot{display:inline-block;width:4px;height:4px;border-radius:50%;background:var(--red)}

/* compliment slip */
.slip{left:266px;top:677px;width:412px;height:197px}
.slip .brand{left:21px;top:25px}
.slip .name{font-size:17px}
.slip .tag{font-size:4.8px;letter-spacing:.66em;margin-top:2px}
.slip-foot{position:absolute;left:0;right:0;top:178px;text-align:center;font-size:6px;color:var(--muted);white-space:nowrap}

/* envelope */
.envelope{left:718px;top:677px;width:412px;height:195px}
.envelope .flap{position:absolute;left:0;top:0;width:412px;height:67px;background:var(--black);clip-path:polygon(0 0,100% 0,98% 100%,2% 100%)}
.envelope .brand{left:0;right:0;top:27px;text-align:center}
.envelope .name{font-size:14.5px}
.envelope .tag{font-size:4.2px;letter-spacing:.72em;margin-top:2px;padding-left:.72em}

/* email signature */
.email-sign{position:absolute;left:430px;top:958px;width:436px}
.email-sign .brand{position:relative}
.email-sign .name{font-size:18.5px}
.email-sign .tag{font-size:5.6px;letter-spacing:.72em;margin-top:3px}
.email-contacts{margin-top:8px;font-size:8px;line-height:1.15}
.email-contacts li{list-style:none;display:flex;align-items:center;gap:5px}
.email-contacts svg{width:8px;height:8px}
.divider{margin:6px 0 5px;border-top:1px dashed #9a9a9a}
.disclaimer{font-size:6.3px;line-height:1.38;color:var(--black)}
.disclaimer b{font-weight:600}
</style>
</head>
<body>
<div class="stage">

  <section class="sheet letterhead" aria-label="Briefbogen">
    <div class="brand"><span class="name">VELMARDO</span><span class="tag">MASSGESCHNEIDERT</span></div>
    <div class="recipient">
      <p>Herr Lukas Brenner<br>Aurelis GmbH</p>
      <p>Feldbergstr. 42<br>4057 Basel</p>
    </div>
    <div class="date">Basel, 15. Januar, 2016</div>
    <div class="letter-body">
      <p class="greet">Sehr geehrte Damen und Herren,</p>
      <p>Fusce neque mi, consectetuer gravida, convallis ac, varius a, pede. Fusce pellentesque pretium quam. Ut luctus, justo id volutpat iaculis, est diam pulvinar sem, quis bibendum turpis dui eget mauris. Sed in mauris. Ut massa. Pellentesque condimentum felis nec sapien. Integer posuere elit at turpis. Nulla facilisi. Sed sapien ipsum, commodo ut, facilisis vitae, ultrices non, metus. Aenean non nulla. Curabitur molestie volutpat magna. Vestibulum tempor faucibus nisi. Pellentesque vitae enim.</p>
      <p>Aliquam rhoncus volutpat mauris. Sed auctor. Donec tincidunt velit et tellus. Donec sed augue eget lacus placerat adipiscing. Ut convallis suscipit nulla. Morbi posuere ullamcorper ligula. Duis sit amet odio nec lorem ornare gravida. Suspendisse ante nulla, gravida quis, eleifend sit amet, placerat eget, purus. Sed egestas magna ut erat. Vivamus euismod, odio id mattis porttitor, tellus nisl consectetuer turpis, ut auctor enim justo euismod nulla. Fusce eget diam vulputate massa tempor tempor.</p>
      <p>In ante. Phasellus convallis, nisl in vestibulum facilisis, lacus pede bibendum urna, dapibus pellentesque eros magna sed nibh. Etiam tortor arcu, porta nec, laoreet quis, mollis in, libero. Aenean dapibus est a metus. In sit amet elit. Pellentesque luctus lacus scelerisque arcu. Morbi posuere ullamcorper ligula. Duis sit amet odio nec lorem ornare gravida. Suspendisse ante nulla, gravida quis, eleifend sit amet, placerat eget, purus.</p>
      <p class="close">Mit freundlichen Grüßen,</p>
    </div>
    <div class="signer">Name Surname<small>Director</small></div>
    <div class="signature" role="img" aria-label="Handschriftliche Unterschrift"></div>
    <div class="letter-foot">
      <div class="co">VELMARDO AG</div>
      <div class="rule"></div>
      <div class="addr">Sonnwiesweg 27, 4068 Basel, Switzerland • T: +41 61 508 37 14 • E: info@velmardo.com • W: www.velmardo.ch • VAT: CHE-472.916.503 MwSt</div>
    </div>
  </section>

  <section class="sheet folder" aria-label="Präsentationsmappe">
    <div class="brand on-dark"><span class="name">VELMARDO</span><span class="tag">MASSGESCHNEIDERT</span></div>
  </section>

  <section class="sheet card card-front" aria-label="Visitenkarte Vorderseite">
    <div class="brand on-dark"><span class="name">VELMARDO</span><span class="tag">MASSGESCHNEIDERT</span></div>
  </section>

  <section class="sheet card card-back" aria-label="Visitenkarte Rückseite">
    <div class="brand"><span class="name">VELMARDO</span><span class="tag">MASSGESCHNEIDERT</span></div>
    <div class="card-person">Name Surname</div>
    <ul class="card-contact left">
      <li><span class="dot"></span>+41 61 508 37 14</li>
      <li><span class="dot"></span>+41 79 842 07 91</li>
      <li><span class="dot"></span>info@velmardo.com</li>
      <li><span class="dot"></span>www.velmardo.ch</li>
    </ul>
    <ul class="card-contact right">
      <li><span class="dot"></span>VELMARDO AG</li>
      <li style="padding-left:7px">Sonnwiesweg 27</li>
      <li style="padding-left:7px">4068 Basel</li>
      <li style="padding-left:7px">Switzerland</li>
    </ul>
  </section>

  <section class="sheet slip" aria-label="Kurzmitteilung">
    <div class="brand"><span class="name">VELMARDO</span><span class="tag">MASSGESCHNEIDERT</span></div>
    <div class="slip-foot">Sonnwiesweg 27, 4068 Basel, Switzerland • T: +41 61 508 37 14 • E: info@velmardo.com • W: www.velmardo.ch</div>
  </section>

  <section class="sheet envelope" aria-label="Briefumschlag">
    <div class="flap"></div>
    <div class="brand on-dark"><span class="name">VELMARDO</span><span class="tag">MASSGESCHNEIDERT</span></div>
  </section>
</div>

<section class="email-sign" aria-label="E-Mail-Signatur">
  <div class="brand"><span class="name">VELMARDO</span><span class="tag">MASSGESCHNEIDERT</span></div>
  <ul class="email-contacts">
    <li><svg viewBox="0 0 8 8"><circle cx="4" cy="4" r="4" fill="#ec1f27"/><path d="M2.6 2.2l.8.8-.4.6a3 3 0 0 0 1.4 1.4l.6-.4.8.8-.6.6c-1.6 0-3.2-1.6-3.2-3.2z" fill="#fff"/></svg>+41 61 508 37 14</li>
    <li><svg viewBox="0 0 8 8"><circle cx="4" cy="4" r="4" fill="#ec1f27"/><rect x="2.8" y="1.8" width="2.4" height="4.4" rx=".4" fill="none" stroke="#fff" stroke-width=".6"/></svg>+41 79 842 07 91</li>
    <li><svg viewBox="0 0 8 8"><circle cx="4" cy="4" r="4" fill="#ec1f27"/><rect x="2" y="2.6" width="4" height="2.8" fill="none" stroke="#fff" stroke-width=".6"/><path d="M2 2.6l2 1.6 2-1.6" fill="none" stroke="#fff" stroke-width=".6"/></svg>info@velmardo.com</li>
    <li><svg viewBox="0 0 8 8"><circle cx="4" cy="4" r="4" fill="#ec1f27"/><circle cx="4" cy="4" r="2" fill="none" stroke="#fff" stroke-width=".6"/><path d="M2 4h4M4 2v4" stroke="#fff" stroke-width=".5"/></svg>www.velmardo.ch</li>
  </ul>
  <div class="divider"></div>
  <p class="disclaimer"><b>Disclaimer:</b> This e-mail is intended solely for the named addressee. If you have received this e-mail in error, please notify the sender, and permanently delete the original and its copies and all attachments. <b>VELMARDO AG</b> accepts no liability for the content of this e-mail, or for the consequences of actions taken on the basis of the information provided. <b>VELMARDO AG</b> accepts no liability for any potential damage caused by reading and forwarding of this e-mail.</p>
</section>
</body>
</html>
```